Veltrano Community Development Planning New web site

Design a new web site. I have a budget of $1,500.00.
Attached on PowerPoint is a complete site plan. Home page and linked pages.
10 - 12 pages. All copy and photos will be supplied. (300dpi)
I have shown them the concept which they like.
No data bases required. Home page with animations dissolving.
They former web site has been taken down. They have been in business 30 years in New Jersey
Colors teal blues and greens
There will be a new logo)being designed)
The text in home page copy will give you a detailed story what they are all about.

files have been approved for Veltrano, Inc.   Tomas is the designer

Industry/Entity Type

Community

```html
<!DOCTYPE html>
<html lang="en">
<head>
<meta charset="utf-8">
<title>Veltrano Inc. — Community Development Planning</title>
<link href="https://fonts.googleapis.com/css2?family=Ubuntu:wght@400;500;700&display=swap" rel="stylesheet">
<style>
  :root{
    --navy-deep:#0b1d36;
    --navy:#12325a;
    --blue-glow:#2a6aa6;
    --panel:rgba(10,26,50,.72);
    --green:#72d94f;
    --green-dark:#5cc23b;
    --white:#ffffff;
    --text:#e6edf5;
    --muted:#9fb3c8;
  }
  *{box-sizing:border-box;margin:0;padding:0}
  html,body{width:988px;height:1200px;overflow:hidden}
  body{
    position:relative;
    font-family:"Ubuntu",sans-serif;
    color:var(--text);
    background:radial-gradient(ellipse 75% 55% at 50% 62%, var(--blue-glow) 0%, var(--navy) 45%, var(--navy-deep) 100%);
  }
  .brand{position:absolute;left:120px;top:20px;font-size:26px;font-weight:700;letter-spacing:2px;color:var(--white)}
  .search{position:absolute;left:705px;top:23px;width:162px;height:20px;background:#0e2443;border:1px solid #1c3b63;
    font-size:9px;font-style:italic;color:var(--muted);padding:4px 13px}
  .search svg{position:absolute;right:6px;top:4px}
  .nav{position:absolute;left:120px;top:66px;width:748px;height:34px;background:var(--green);
    display:flex;justify-content:center;gap:35px;align-items:center}
  .nav a{color:var(--white);font-size:9px;font-weight:700;text-decoration:none;letter-spacing:.2px}
  .hero{position:absolute;left:120px;top:116px;width:748px;height:346px;border:2px solid #dfe8f2;
    background:radial-gradient(ellipse 60% 70% at 60% 50%, #4fa3e8 0%, #1c5a9c 40%, #0a2244 100%)}
  .dots{position:absolute;right:50px;bottom:22px;display:flex;gap:5px}
  .dots span{width:9px;height:9px;border-radius:50%;background:#b9c6d4}
  .dots span:first-child{background:var(--white)}
  .services{position:absolute;left:120px;top:478px;width:749px;display:flex;gap:23px}
  .service{width:170px;height:59px;background:var(--green);color:var(--white);font-size:10.5px;font-weight:500;
    text-align:center;display:flex;align-items:center;justify-content:center;line-height:1.25;box-shadow:0 2px 4px rgba(0,0,0,.35)}
  .panel{position:absolute;top:571px;width:362px;height:482px;
    background:linear-gradient(to bottom, var(--panel) 0%, rgba(10,26,50,.55) 70%, rgba(10,26,50,0) 100%)}
  .panel.about{left:120px;padding:35px 33px 0 35px}
  .panel.results{left:506px;padding:30px 34px 0 36px}
  .about p{font-size:12px;line-height:1.23;margin-bottom:17px}
  .seal{position:absolute;left:35px;top:246px;width:78px;height:78px;border-radius:50%;border:2px solid #dfe8f2}
  .info{position:absolute;left:131px;font-size:10.3px;font-weight:500;line-height:1.25}
  .info .url{font-weight:400;display:block}
  .contact{position:absolute;left:131px;display:flex;align-items:center;gap:14px;font-size:12px}
  .results h2{font-size:26px;font-weight:500;color:var(--white);text-align:center;margin-bottom:26px}
  .results ul{list-style:none}
  .results li{position:relative;padding-left:20px;font-size:12px;line-height:1.25;margin-bottom:24px}
  .results li::before{content:"";position:absolute;left:2px;top:3px;width:5px;height:5px;border-right:1.6px solid #fff;border-top:1.6px solid #fff;transform:rotate(45deg)}
  .results li.strong{font-weight:700}
  .members{position:absolute;left:120px;top:1116px;width:748px;display:flex;align-items:center;justify-content:space-between}
  .members .label{font-size:10.5px;color:#c9d4e0}
  .members .label b{font-weight:700}
  .badge{background:rgba(190,205,222,.55)}
  .footer{position:absolute;left:0;top:1165px;width:988px;height:35px;background:var(--green);color:var(--white);
    font-size:10.5px;display:flex;align-items:center;padding:0 120px;justify-content:space-between;letter-spacing:.3px}
  .footer span{display:flex;align-items:center;gap:7px}
</style>
</head>
<body>
  <div class="brand">VELTRANO</div>
  <div class="search">Search
    <svg width="11" height="11" viewBox="0 0 12 12"><circle cx="7" cy="5" r="3.6" fill="none" stroke="#9fb3c8" stroke-width="1.4"/><line x1="4.4" y1="7.6" x2="1" y2="11" stroke="#9fb3c8" stroke-width="1.6"/></svg>
  </div>
  <nav class="nav">
    <a href="#">HOME</a><a href="#">OUR COMPANY</a><a href="#">SERVICES</a>
    <a href="#">HOUSING REHAB APPLICATION</a><a href="#">AFFORDABLE APPLICATION</a><a href="#">CONTACT US</a>
  </nav>
  <div class="hero" role="img" aria-label="Slideshow image: glowing blue city buildings and data analysis graphics held over an open hand">
    <div class="dots"><span></span><span></span><span></span><span></span></div>
  </div>
  <div class="services">
    <div class="service">COMMUNITY<br>DEVELOPMENT<br>PLANNING</div>
    <div class="service">HOUSING<br>REHABILITATION<br>ADMINISTRATION</div>
    <div class="service">HUD<br>PROGRAM<br>MANAGEMENT</div>
    <div class="service">COAH<br>PROGRAMS<br>IMPLEMENTATION</div>
  </div>

  <section class="panel about">
    <p>Veltrano Inc. is a city planning firm that specializes in community development and housing rehabilitation program planning, design and implementation. We have over twenty years of experience in developing and administering income base housing and programs in accordance with US Department of Housing and Urban Development (HUD) and New Jersey Council on Affordable Housing (COAH) rules and regulations.</p>
    <p>In addition, our firm is capable of providing the technical and administrative assistance our clients require for implementation of their income based housing programs.</p>
    <div class="seal" role="img" aria-label="Federal housing department seal"></div>
    <div class="info" style="top:260px">TO FIND OUT MORE ABOUT FEDERAL<br>HOUSING PROGRAMS THAT WE WILL<br>ADMINISTER PLEASE GO TO:<span class="url">www.fedhousinginfo.org</span></div>
    <div class="info" style="top:358px">FOR MORE INFORMATION ABOUT<br>OUR SERVICES, PLEASE CONTACT US<br>TODAY AT VELTRANO:</div>
    <div class="contact" style="top:410px">
      <svg width="12" height="17" viewBox="0 0 12 17"><rect x="1" y="1" width="10" height="15" rx="1.5" fill="none" stroke="#fff" stroke-width="1.4"/><line x1="1" y1="13" x2="11" y2="13" stroke="#fff"/></svg>
      (732) 555 0184</div>
    <div class="contact" style="top:440px">
      <span style="font-size:17px">@</span> info@veltranoplanning.com</div>
  </section>

  <section class="panel results">
    <h2>WE GET RESULTS</h2>
    <ul>
      <li>Veltrano designs income based programs to be supported by federal placement lotteries state funding.</li>
      <li>We implement local programs to benefit people seeking access to affordable housing.</li>
      <li>Our experienced staff screen applicants for local affordable housing.</li>
      <li>We pre-qualify persons who have applied for housing rehabilitation.</li>
      <li class="strong">Conduct placement lotteries</li>
      <li>Through local housing rehabilitation programs, our experience construction inspectors determine what improvements are required at eligible units based on local building codes and health and safety issues.</li>
    </ul>
  </section>

  <div class="members">
    <div class="label"><b>VELTRANO</b> INC. IS A MEMBER OF:</div>
    <div class="badge" style="width:135px;height:20px" role="img" aria-label="Member association badge"></div>
    <div class="badge" style="width:38px;height:38px" role="img" aria-label="Member association badge"></div>
    <div class="badge" style="width:38px;height:38px;border-radius:50%" role="img" aria-label="Member association badge"></div>
    <div class="badge" style="width:155px;height:22px" role="img" aria-label="Member association badge"></div>
  </div>

  <footer class="footer">
    <span>Copy Right 2014 &nbsp;&nbsp;<b>VELTRANO</b> INC.</span>
    <span><svg width="12" height="9" viewBox="0 0 12 9"><rect x=".5" y=".5" width="11" height="8" fill="none" stroke="#fff"/><polyline points=".5,.5 6,5 11.5,.5" fill="none" stroke="#fff"/></svg>215 Harbor Crest Lane, Brick, New Jersey, 08724</span>
    <span><svg width="9" height="14" viewBox="0 0 9 14"><rect x=".7" y=".7" width="7.6" height="12.6" rx="1.2" fill="none" stroke="#fff" stroke-width="1.2"/></svg>(732) 555 0184</span>
    <span><b style="font-size:14px;font-weight:400">@</b>info@veltranoplanning.com</span>
  </footer>
</body>
</html>
```